Calloway needs a modernized design

We would like a modern update (that can be responsive) to our existing website. Attached are the two existing pages we would like new concepts of - our home page and a page about one of our locations.

Calloway is provides executive offices and virtual office services. Startups, law firms, and financial services are our primary clients. We would like a professional, clean design, leaning towards minimalist. We intend to greatly reduce/eliminate the long paragraphs of text.

Industry/Entity Type

Business Service

Number of Pages Required

2 page

Requirements
Must have
• A design that can be responsive
Nice to have
• Large image(s) on home page that rotate.

```html
<!DOCTYPE html>
<html lang="en">
<head>
<meta charset="utf-8">
<title>Calloway Business Centers</title>
<link href="https://fonts.googleapis.com/css2?family=Roboto:wght@400;500&display=swap" rel="stylesheet">
<style>
:root{
  --navy:#2c3a6b;
  --navy-text:#2f3d70;
  --white:#ffffff;
  --map-bg:#e7e3da;
}
*{box-sizing:border-box;margin:0;padding:0}
html,body{width:800px;height:1200px;overflow:hidden}
body{font-family:"Roboto",Arial,sans-serif;color:var(--navy-text);background:var(--white);position:relative}
.site-header{position:absolute;top:0;left:0;width:800px;height:74px;background:var(--white);box-shadow:0 2px 5px rgba(0,0,0,.25);z-index:3}
.brand{position:absolute;left:80px;top:10px;display:flex;align-items:center;gap:10px}
.brand-mark{width:55px;height:55px;border-radius:50%;background:var(--navy)}
.brand-name{font-size:24px;font-weight:500;color:var(--navy);letter-spacing:.5px}
.phone{position:absolute;right:80px;top:12px;display:flex;align-items:center;gap:8px;font-size:17px;color:var(--navy)}
.main-nav{position:absolute;right:80px;top:42px;display:flex;gap:9px;font-size:13.5px}
.main-nav a{color:var(--navy);text-decoration:none}
.main-nav a.current{text-decoration:underline;text-underline-offset:3px}
.hero{position:absolute;top:74px;left:0;width:800px;height:718px;
  background:linear-gradient(180deg,#d9dde3 0%,#c9ccd1 25%,#b9a89b 50%,#8b6552 75%,#b79f94 100%)}
.hero-title{position:absolute;top:86px;width:100%;text-align:center;font-size:33px;font-weight:400;color:var(--navy-text)}
.service-grid{position:absolute;top:198px;left:79px;display:grid;grid-template-columns:repeat(3,201px);grid-auto-rows:201px;gap:23px 20px}
.service-tile{background:var(--white);box-shadow:0 2px 4px rgba(0,0,0,.3);display:flex;flex-direction:column;align-items:center;padding-top:18px;text-align:center;font-size:27px;line-height:33px;color:var(--navy-text)}
.service-tile svg{height:78px;margin-bottom:12px;fill:var(--navy)}
.service-tile.active{background:var(--navy);color:var(--white)}
.service-tile.active svg{fill:var(--white)}
.location{position:absolute;top:792px;width:800px;text-align:center}
.divider{display:flex;justify-content:center;align-items:center;gap:4px;margin-top:19px}
.divider span{width:80px;height:6px;background:var(--navy)}
.divider i{width:32px;height:32px;border-radius:50%;background:var(--navy)}
.location h2{font-size:23px;font-weight:400;margin-top:12px;letter-spacing:.2px}
.location p{font-size:19px;margin-top:14px}
.map-area{position:absolute;top:948px;left:0;width:800px;height:252px;background:linear-gradient(135deg,#e9e5dc,#dcd8cf 60%,#cfe0c2)}
.map-title{position:absolute;top:48px;width:100%;text-align:center;font-size:32px;color:var(--navy-text)}
</style>
</head>
<body>
<header class="site-header">
  <div class="brand"><div class="brand-mark"></div><span class="brand-name">Calloway</span></div>
  <div class="phone">
    <svg width="20" height="20" viewBox="0 0 20 20"><circle cx="10" cy="10" r="9" fill="none" stroke="#2c3a6b" stroke-width="1.5"/><path d="M6.5 5.5l2 0 .8 2.3-1.2 1c.6 1.3 1.5 2.2 2.8 2.8l1-1.2 2.3.8v2c-4.5.3-8-3.2-7.7-7.7z" fill="#2c3a6b"/></svg>
    214-555-0147
  </div>
  <nav class="main-nav">
    <a class="current" href="#">Home</a><a href="#">Properties</a><a href="#">Virtual Tours &amp; Videos</a><a href="#">Photos</a><a href="#">Broker Referrals</a>
  </nav>
</header>

<section class="hero" role="img" aria-label="Blurred photo of a bright office lobby with wood furniture">
  <h1 class="hero-title">How can we surve you?</h1>
  <div class="service-grid">
    <div class="service-tile active">
      <svg viewBox="0 0 60 80"><path d="M14 0h32l-8 10 14 50-22 20-12-22 10-48z"/></svg>
      Executive<br>office<br>suites
    </div>
    <div class="service-tile">
      <svg viewBox="0 0 80 60" fill="none" stroke="#2c3a6b" stroke-width="3"><circle cx="40" cy="8" r="6"/><circle cx="14" cy="22" r="6"/><circle cx="66" cy="22" r="6"/><rect x="22" y="26" width="36" height="30"/><path d="M4 40h14M62 40h14M8 58v-18M72 58v-18"/></svg>
      On-demand<br>meeting<br>rooms
    </div>
    <div class="service-tile">
      <svg viewBox="0 0 90 60"><circle cx="66" cy="14" r="12"/><path d="M2 40L30 14l20 4-8 10 16 12z"/><path d="M0 52q8-8 15 0t15 0 15 0 15 0 15 0 15 0v6H0z"/></svg>
      On-demand<br>training<br>rooms
    </div>
    <div class="service-tile">
      <svg viewBox="0 0 90 80"><path d="M33 4h24v10h-5V9H38v5h-5z"/><rect x="0" y="14" width="90" height="66" rx="4"/><rect x="36" y="38" width="18" height="12" fill="#fff"/><rect x="40" y="41" width="10" height="6"/></svg>
      Virtual office<br>solutions
    </div>
    <div class="service-tile">
      <svg viewBox="0 0 96 72"><rect x="2" y="2" width="92" height="56" fill="none" stroke="#2c3a6b" stroke-width="4"/><path d="M40 18l20 12-20 12z"/><rect x="28" y="64" width="40" height="5"/></svg>
      Video<br>Conference<br>solutions
    </div>
    <div class="service-tile">
      <svg viewBox="0 0 80 80"><circle cx="40" cy="40" r="39"/><circle cx="40" cy="20" r="6" fill="#fff"/><path d="M32 32h13v28h5v5H30v-5h5V37h-3z" fill="#fff"/></svg>
      request more<br>information
    </div>
  </div>
</section>

<section class="location">
  <div class="divider"><span></span><i></i><span></span></div>
  <h2>UPTOWN HOLLOWAY AVENUE EXECUTIVE OFFICE SUITES</h2>
  <p>All Inclusive Executive Office Suites from $495/mo</p>
</section>

<section class="map-area" role="img" aria-label="Street map showing the uptown office location">
  <div class="map-title">We are here to help!</div>
</section>
</body>
</html>
```